Healthcare and Professional IT Services Company need a redesigned business card

We are a IT Services company that targets small medical practices and professional business such as Attorneys, Accounts, Architects etc. We want to communicate a professional yet friendly image using recent logo redesign here on Drafthive. Like to see the colors blue and orange in the design. Must use the Tall Cedar Technology as displayed in the new logo - then also want to incorporate the fish logo as well.

Target Market(s)

Small medical and professional services

Industry/Entity Type

It Company

Contact Information for Business Card

The usual stuff, place for name address phone website. Also maybe our tagline which is "hooked on technology"

Requirements
Must have
• My new logo and the fish somewhere on the card

```html
<!DOCTYPE html>
<html lang="en">
<head>
<meta charset="utf-8">
<title>Tall Cedar Technology – Business Card</title>
<link rel="stylesheet" href="https://fonts.googleapis.com/css2?family=Open+Sans:wght@400;600;700&display=swap">
<style>
  :root {
    --backdrop: #1d1d1f;
    --blue-deep: #1566c9;
    --blue-light: #3b9ae0;
    --blue-text: #2a86d6;
    --blue-faint: rgba(255,255,255,0.14);
    --ink: #3a3a3a;
    --paper: #ffffff;
    --orange: #f39a1e;
  }
  * { margin: 0; padding: 0; box-sizing: border-box; }
  html, body {
    width: 1200px; height: 900px; overflow: hidden;
    background: var(--backdrop);
    font-family: "Open Sans", Arial, sans-serif;
  }
  .stage {
    width: 1200px; height: 900px;
    display: flex; flex-direction: column; align-items: center; justify-content: center;
    gap: 36px;
  }
  .card {
    width: 700px; height: 400px; position: relative; overflow: hidden;
    box-shadow: 0 10px 30px rgba(0,0,0,0.5);
  }
  /* Front */
  .card--front {
    background: linear-gradient(90deg, var(--blue-deep) 0%, var(--blue-light) 100%);
  }
  .front__mascot {
    position: absolute; left: 40px; top: 40px; width: 400px; height: 300px;
    border-radius: 50% 45% 40% 50%;
    background: radial-gradient(ellipse at 60% 45%, var(--blue-faint), rgba(255,255,255,0) 70%);
  }
  .front__brand {
    position: absolute; right: 48px; bottom: 70px;
    color: var(--paper); font-weight: 700; font-size: 34px; letter-spacing: -0.5px;
  }
  /* Back */
  .card--back { background: var(--paper); }
  .back__mascot {
    position: absolute; left: 50%; top: 30px; transform: translateX(-50%);
    width: 230px; height: 120px; border-radius: 45%;
    background: radial-gradient(ellipse at 60% 50%, #cfe6fa, #eaf4fd 70%, rgba(255,255,255,0));
  }
  .back__brand {
    position: absolute; top: 165px; left: 0; right: 0; text-align: center;
    color: var(--blue-text); font-weight: 700; font-size: 34px; letter-spacing: -0.5px;
  }
  .contact {
    position: absolute; top: 240px; left: 0; right: 0;
    display: flex; flex-direction: column; align-items: center; gap: 10px;
    color: var(--ink); font-size: 18px;
  }
  .contact__row { display: flex; align-items: center; gap: 10px; }
  .contact__name { color: var(--blue-text); font-weight: 700; }
  .contact__role { font-weight: 400; }
  .contact__dot { width: 5px; height: 5px; border-radius: 50%; background: var(--ink); }
  .contact__item { display: inline-flex; align-items: center; gap: 6px; }
  .icon { width: 16px; height: 16px; fill: none; stroke: var(--blue-text); stroke-width: 2; }
</style>
</head>
<body>
<main class="stage">
  <section class="card card--front">
    <div class="front__mascot" role="img" aria-label="Faint outline of the fish mascot"></div>
    <div class="front__brand">Tall Cedar Technology</div>
  </section>

  <section class="card card--back">
    <div class="back__mascot" role="img" aria-label="Cartoon fish mascot in blue outline"></div>
    <div class="back__brand">Tall Cedar Technology</div>
    <div class="contact">
      <div class="contact__row">
        <span class="contact__name">Dana Reyes</span>
        <span class="contact__dot"></span>
        <span class="contact__role">Manager</span>
      </div>
      <div class="contact__row">
        <span class="contact__item">
          <svg class="icon" viewBox="0 0 16 16"><path d="M4 2 L6 5 L5 7 Q7 10 9 11 L11 10 L14 12 L12 14 Q6 13 2 4 Z"/></svg>
          555 014 2290
        </span>
        <span class="contact__item">
          <svg class="icon" viewBox="0 0 16 16"><circle cx="8" cy="8" r="6"/><ellipse cx="8" cy="8" rx="2.5" ry="6"/><line x1="2" y1="8" x2="14" y2="8"/></svg>
          www.danareyes.com
        </span>
      </div>
      <div class="contact__row">
        <span class="contact__item">
          <svg class="icon" viewBox="0 0 16 16"><circle cx="8" cy="8" r="2.5"/><path d="M10.5 8 V9.5 Q10.5 11 12 11 Q14 11 14 8 A6 6 0 1 0 11 13"/></svg>
          dana@tallcedartech.com
        </span>
      </div>
    </div>
  </section>
</main>
</body>
</html>
```